Unternehmen für Ordnung und Sauberkeit am Arbeitsplatz und Produkte zur Produktionsoptimierung benötigt Visitenkarten und Briefpapier
Zielgruppe
Produkte für Ordnung und Sauberkeit am Arbeitsplatz, Organisation von Arbeitsplätzen, Produkte zur Vereinfachung von Arbeitsabläufen, Produkte zur Produktionsoptimierung unter dem Lean Gedanke, Schlagwort: "5S", nachhaltig, sauber
Aufgabenstellung
Wir sind auf der Suche nach Visitenkarten und Briefpapier für das Unternehmen ourKarto. Nachhaltig, Sauber usw.. Unser Firmenlogo finden Sie anbei.

```html
<!DOCTYPE html>
<html lang="de">
<head>
<meta charset="utf-8">
<title>ourKarto – Visitenkarte</title>
<link rel="stylesheet" href="https://fonts.googleapis.com/css2?family=Fira+Sans:wght@400;600&display=swap">
<style>
  :root {
    --brand-green: #1e8443;
    --page-bg: #ececec;
    --card-white: #ffffff;
    --ink: #1c1c1c;
    --ghost-grey: #e2e2e2;
    --card-shadow: 0 2px 6px rgba(0, 0, 0, 0.25);
  }
  * { box-sizing: border-box; margin: 0; padding: 0; }
  html, body {
    width: 1163px;
    height: 1200px;
    overflow: hidden;
    background: var(--page-bg);
    font-family: "Fira Sans", Arial, sans-serif;
  }
  .canvas { position: relative; width: 1163px; height: 1200px; }

  .card { position: absolute; width: 725px; height: 416px; box-shadow: var(--card-shadow); overflow: hidden; }
  .card--front { left: 156px; top: 202px; background: var(--card-white); }
  .card--back { left: 295px; top: 681px; width: 721px; height: 417px; background: var(--brand-green); }

  .ghost-mark {
    position: absolute;
    left: 20px;
    top: 90px;
    display: flex;
    align-items: center;
    gap: 18px;
    color: var(--ghost-grey);
    font-weight: 600;
    font-size: 92px;
    line-height: 1;
  }
  .ghost-mark__square { width: 70px; height: 70px; background: var(--ghost-grey); }

  .person { position: absolute; right: 281px; top: 178px; text-align: right; }
  .person__name { font-size: 19px; font-weight: 600; color: var(--ink); }
  .person__role { font-size: 15px; color: var(--ink); margin-top: 8px; }

  .divider { position: absolute; left: 469px; top: 180px; width: 3px; height: 196px; background: var(--brand-green); }

  .contact { position: absolute; left: 493px; font-size: 16px; color: var(--ink); line-height: 23px; }
  .contact--address { top: 186px; }
  .contact--web { top: 262px; }
  .contact--phone { top: 331px; }
  .contact__row { display: flex; align-items: center; }
  .contact__icon { width: 32px; display: flex; align-items: center; }
  .contact__icon svg { fill: var(--brand-green); }
  .contact__row--indent { padding-left: 32px; }

  .card__band { position: absolute; left: 0; bottom: 0; width: 100%; height: 15px; background: var(--brand-green); }

  .brand-mark {
    position: absolute;
    left: 50%;
    top: 50%;
    transform: translate(-50%, -50%);
    display: flex;
    align-items: center;
    gap: 16px;
    color: var(--card-white);
    font-weight: 600;
    font-size: 62px;
    line-height: 1;
  }
  .brand-mark__circle { width: 54px; height: 54px; border-radius: 50%; background: var(--card-white); }
</style>
</head>
<body>
<main class="canvas">
  <section class="card card--front" aria-label="Visitenkarte Vorderseite">
    <div class="ghost-mark" aria-hidden="true">
      <span class="ghost-mark__square"></span>
      <span>ourKarto</span>
    </div>

    <div class="person">
      <p class="person__name">Lena Beispiel</p>
      <p class="person__role">Geschäftsführerin</p>
    </div>

    <div class="divider"></div>

    <div class="contact contact--address">
      <p class="contact__row">
        <span class="contact__icon"><svg width="12" height="16" viewBox="0 0 12 16"><path d="M6 0a6 6 0 0 0-6 6c0 4.5 6 10 6 10s6-5.5 6-10a6 6 0 0 0-6-6zm0 8.5A2.5 2.5 0 1 1 6 3.5a2.5 2.5 0 0 1 0 5z"/></svg></span>
        Ahornweg 12
      </p>
      <p class="contact__row contact__row--indent">79312 Waldhofen</p>
    </div>

    <div class="contact contact--web">
      <p class="contact__row">
        <span class="contact__icon"><svg width="13" height="10" viewBox="0 0 13 10"><path d="M0 0h13v1.5L6.5 5.5 0 1.5z"/><path d="M0 3l6.5 4L13 3v7H0z"/></svg></span>
        info@ourkarto.de
      </p>
      <p class="contact__row">
        <span class="contact__icon"><svg width="13" height="13" viewBox="0 0 13 13"><circle cx="6.5" cy="6.5" r="5.8" fill="none" stroke="#1e8443" stroke-width="1.2"/><ellipse cx="6.5" cy="6.5" rx="2.4" ry="5.8" fill="none" stroke="#1e8443" stroke-width="1.1"/><path d="M0.8 6.5h11.4" stroke="#1e8443" stroke-width="1.1"/></svg></span>
        www.ourkarto.de
      </p>
    </div>

    <div class="contact contact--phone">
      <p class="contact__row">
        <span class="contact__icon"><svg width="15" height="12" viewBox="0 0 15 12"><path d="M0 4c0-2 3-4 7.5-4S15 2 15 4v1.5h-4V3.5h-7V5.5H0z"/><path d="M3 7h9l1 5H2z"/></svg></span>
        0 21 34 / 56 78 90
      </p>
      <p class="contact__row">
        <span class="contact__icon"><svg width="15" height="13" viewBox="0 0 15 13"><rect x="4" y="0" width="7" height="4"/><rect x="0" y="5" width="15" height="8" rx="1"/></svg></span>
        0 43 21 / 12 34 567
      </p>
    </div>

    <div class="card__band"></div>
  </section>

  <section class="card card--back" aria-label="Visitenkarte Rückseite">
    <div class="brand-mark">
      <span class="brand-mark__circle"></span>
      <span>ourKarto</span>
    </div>
  </section>
</main>
</body>
</html>
```